6 page (for now) squarespace website design for a Mobile Fitness small business

My sons California based small business "Brindle Motion Coaching" with new subsidiary called "Brindle Motion 4 Kids". I don't understand coding the website, is that the function squarespace provides?
In the end I want a working website, squarespace, I have a google workspace domain, email and subscription to squarespace & google workspace. URLs include brindlemotioncoaching.example and brindlemotion4kids.example. I have an idea of what I am looking for in a website and I have some examples of website designs I like, but I am 100% open to your design concepts and artistic flair. email is corwin@brindlemotioncoaching.example
I am looking for someone to design the site, help me understand how to make "minor" changes and hopefully have a long term relationship on the tech side of the business. I need an Idea of pricing for future changes (Rate T&M).
There are 2 businesses so I need a way to incorporate both the main company and a subsidiary into 1 website or link it somehow. I am open to your suggestions how to accomplish that. Do I need 2 completely separate websites or can it be done on 1 site directing you to different pages. I read conflicting info if it is a BAD idea to link 2 different websites so I will defer to your advice.
Below are the pages I need designed:
- Home Page- Brindle Motion Coaching
- Home Page- Brindle Motion 4 Kids (Homeschool market)
- Member Page (subscription service?)
- Workouts- with video clips 1-6 min each
- About
- Contact
- FAQ's
Future work & page designs:
- Store with training subscriptions & a few merch items
- Booking Appointments
- Bookshelf
- email campaign
-Blog
I like the feel of this website:
https://quellpace.example/

```html
<!DOCTYPE html>
<html lang="en">
<head>
<meta charset="utf-8">
<title>Membership · Brindle Motion</title>
<link href="https://fonts.googleapis.com/css2?family=Rajdhani:wght@700&family=Montserrat:wght@400;500;600;700&display=swap" rel="stylesheet">
<style>
:root{
  --bg-header:#1e1f23;
  --bg-dark:#0c0b0b;
  --bg-section:#1f2024;
  --bg-footer:#1c1d21;
  --white:#ffffff;
  --muted:#8a8b90;
  --nav:#9a9ba0;
  --orange:#f7941d;
  --orange-deep:#f26522;
  --orange-light:#fbb040;
  --price:#d0021b;
  --tick:#8dc63f;
  --teal:#1fbf8f;
  --card-text:#7d7d7d;
  --black:#000000;
}
*{box-sizing:border-box;margin:0;padding:0}
html,body{width:1200px;height:2609px;overflow:hidden;background:var(--bg-dark)}
body{position:relative;font-family:'Montserrat',sans-serif;color:var(--white)}

/* header */
.site-header{position:absolute;left:0;top:0;width:1200px;height:63px;background:var(--bg-header)}
.brand{position:absolute;left:46px;top:10px;display:flex;align-items:center;gap:14px}
.brand-dot{width:40px;height:40px;border-radius:50%;border:2px solid var(--white)}
.brand-name{font-family:'Montserrat',sans-serif;font-weight:500;font-size:19px;letter-spacing:4px;color:var(--white);white-space:nowrap}
.main-nav{position:absolute;left:381px;top:26px;display:flex;gap:30px}
.main-nav a{font-size:10px;letter-spacing:2px;color:var(--nav);text-decoration:none;font-weight:500}
.main-nav a.active{color:var(--white);font-weight:700;padding-bottom:8px;border-bottom:2px solid var(--orange)}
.header-social{position:absolute;left:1092px;top:26px;display:flex;gap:10px;align-items:center}
.soc-dot{width:11px;height:11px;border-radius:50%;background:var(--nav)}

/* hero */
.hero{position:absolute;left:0;top:63px;width:1200px;height:453px;background:linear-gradient(90deg,#050505 0%,#0b0a0a 45%,#3a2f2a 75%,#5a4a42 100%)}
.hero-photo{position:absolute;right:0;top:0;width:520px;height:453px;background:radial-gradient(ellipse at 55% 50%,#6a5850 0%,#3a302b 45%,rgba(10,9,9,0) 80%)}
.hero-title{position:absolute;left:0;width:1200px;top:170px;text-align:center;font-family:'Rajdhani',sans-serif;font-weight:700;font-size:60px;letter-spacing:2px}

/* pricing */
.pricing{position:absolute;left:0;top:516px;width:1200px;height:625px;background:radial-gradient(ellipse at 40% 40%,#3d3129 0%,#1a1512 45%,#0d0b0a 80%)}
.section-title{position:absolute;left:0;width:1200px;text-align:center;font-family:'Rajdhani',sans-serif;font-weight:700;font-size:33px;letter-spacing:1px}
.section-sub{position:absolute;left:0;width:1200px;text-align:center;font-size:12px;letter-spacing:1px;color:var(--muted)}
.plan{position:absolute;top:189px;width:168px;height:336px;background:var(--white);color:var(--black);padding:20px 21px 0}
.plan.featured{background:linear-gradient(160deg,var(--orange-deep) 0%,var(--orange) 55%,var(--orange-light) 100%);color:var(--white)}
.plan-name{font-size:9px;font-weight:700;letter-spacing:.5px}
.plan-price{margin-top:10px;display:flex;align-items:baseline;gap:8px}
.plan-price strong{font-size:24px;font-weight:700;color:var(--price)}
.plan.featured .plan-price strong{color:var(--white)}
.plan-price span{font-size:11px;color:var(--card-text)}
.plan.featured .plan-price span,.plan.featured .plan-desc,.plan.featured .plan-features li{color:var(--white)}
.plan-desc{margin-top:9px;font-size:9.5px;line-height:15px;color:var(--card-text);padding-bottom:2px;border-bottom:1px dotted #c8c8c8}
.plan.featured .plan-desc{border-bottom-color:rgba(255,255,255,.6)}
.plan-features{list-style:none;margin-top:17px}
.plan-features li{font-size:9.5px;line-height:22.5px;color:#333;display:flex;align-items:center;gap:10px}
.plan-features svg{flex:none}
.plan-btn{position:absolute;left:21px;top:276px;width:125px;height:28px;background:var(--black);color:var(--white);font-size:8.5px;font-weight:700;letter-spacing:.5px;display:flex;align-items:center;justify-content:center}

/* trainers */
.trainers{position:absolute;left:0;top:1141px;width:1200px;height:748px;background:var(--bg-section)}
.trainer{position:absolute;top:204px;width:325px;height:375px;text-align:center}
.trainer-photo{position:absolute;inset:0}
.trainer-1 .trainer-photo{background:linear-gradient(180deg,#d3902f 0%,#e58a3c 50%,#f0875a 100%)}
.trainer-2 .trainer-photo{background:radial-gradient(ellipse at 55% 35%,#6b6b6b 0%,#2a2a2a 55%,#111 100%)}
.trainer-3 .trainer-photo{background:linear-gradient(180deg,rgba(0,0,0,0) 60%,#2a2524 82%,#1a1716 100%),radial-gradient(ellipse at 50% 35%,#b89a88 0%,#d8d4d0 50%,#ececec 100%)}
.trainer-label{position:absolute;left:0;width:100%}
.trainer-role{font-family:'Rajdhani',sans-serif;font-weight:700;font-size:23px;color:var(--white);letter-spacing:.5px}
.trainer-name{font-size:13px;font-weight:700;letter-spacing:.5px;color:var(--white);margin-top:9px}
.trainer-bio{font-size:11px;line-height:18.5px;margin:13px auto 0;width:250px}
.trainer-more{font-size:11px;font-weight:700;letter-spacing:1.5px;margin-top:40px}
.dots{position:absolute;top:643px;left:0;width:1200px;display:flex;justify-content:center;gap:20px}
.dots i{width:10px;height:10px;border-radius:50%;background:#8a8a8e}
.dots i.on{background:var(--orange)}

/* cta */
.cta{position:absolute;left:0;top:1889px;width:1200px;height:438px;background:radial-gradient(ellipse at 50% 55%,#4a3b33 0%,#241d19 45%,#141210 80%)}
.cta-lines{position:absolute;left:0;width:1200px;top:88px;text-align:center;font-family:'Rajdhani',sans-serif;font-weight:700;font-size:66px;line-height:62.5px;letter-spacing:1px}
.cta-lines .accent{color:var(--orange)}
.cta-btn{position:absolute;left:521px;top:357px;width:158px;height:40px;background:linear-gradient(90deg,var(--orange-deep),var(--orange-light));font-size:13px;font-weight:600;letter-spacing:.5px;display:flex;align-items:center;justify-content:center}

/* footer */
.site-footer{position:absolute;left:0;top:2327px;width:1200px;height:282px;background:var(--bg-footer)}
.contact-col{position:absolute;top:42px}
.contact-label{font-size:10.5px;font-weight:700;font-style:italic;letter-spacing:.5px}
.contact-label::after{content:"";display:block;width:19px;height:2px;background:var(--teal);margin-top:5px}
.contact-value{margin-top:25px;font-size:12px;letter-spacing:.3px;white-space:nowrap}
.contact-value.email{font-size:11px;letter-spacing:0}
.footer-social{display:flex;gap:18px;margin-top:20px;align-items:center}
.footer-social .soc-dot{width:15px;height:15px;background:#cfd0d3}
.footer-brand{position:absolute;left:0;width:1200px;top:138px;display:flex;flex-direction:column;align-items:center}
.footer-brand .brand-dot{width:54px;height:54px}
.footer-brand .brand-name{font-size:17px;margin-top:10px}
.footer-nav{position:absolute;left:0;width:1200px;top:245px;display:flex;justify-content:center;gap:30px}
.footer-nav a{font-size:9.5px;letter-spacing:2.5px;color:#7d7e83;text-decoration:none;font-weight:500}
</style>
</head>
<body>

<header class="site-header">
  <div class="brand"><span class="brand-dot"></span><span class="brand-name">BRINDLE MOTION</span></div>
  <nav class="main-nav">
    <a href="#">HOME</a><a href="#">ABOUT</a><a href="#">WORKOUTS</a><a href="#" class="active">MEMBERSHIP</a><a href="#">SHOP</a><a href="#">CONTACT</a>
  </nav>
  <div class="header-social">
    <span class="soc-dot"></span><span class="soc-dot"></span><span class="soc-dot"></span>
    <svg width="12" height="9" viewBox="0 0 12 9"><rect x=".5" y=".5" width="11" height="8" fill="none" stroke="#9a9ba0"/><path d="M.5 .5 6 5l5.5-4.5" fill="none" stroke="#9a9ba0"/></svg>
  </div>
</header>

<section class="hero">
  <div class="hero-photo" role="img" aria-label="Athlete in a sports top standing against a dark backdrop"></div>
  <h1 class="hero-title">MEMBERSHIP</h1>
</section>

<section class="pricing" role="img" aria-label="Dim background photo of a training athlete">
  <h2 class="section-title" style="top:70px">MEMBERSHIP PLAN &amp; PRICE</h2>
  <p class="section-sub" style="top:126px">LOREM IPSUM DOLOR SIT AMET</p>

  <article class="plan" style="left:235px">
    <div class="plan-name">PERSONAL</div>
    <div class="plan-price"><strong>$49</strong><span>/ Month</span></div>
    <p class="plan-desc">Lorem ipsum dolor sit ametLorem ipsum dolor sit amet, consectetue</p>
    <ul class="plan-features">
      <li><svg width="8" height="6" viewBox="0 0 8 6"><path d="M1 3l2 2 4-4" fill="none" stroke="#8dc63f" stroke-width="1.2"/></svg>5 Times trial</li>
      <li><svg width="8" height="6" viewBox="0 0 8 6"><path d="M1 3l2 2 4-4" fill="none" stroke="#8dc63f" stroke-width="1.2"/></svg>Use all equipments</li>
      <li><svg width="8" height="6" viewBox="0 0 8 6"><path d="M1 3l2 2 4-4" fill="none" stroke="#8dc63f" stroke-width="1.2"/></svg>Advice from trainer</li>
    </ul>
    <div class="plan-btn">REGISTER NOW</div>
  </article>

  <article class="plan featured" style="left:422px">
    <div class="plan-name">GROUP</div>
    <div class="plan-price"><strong>$79</strong><span>/ Month</span></div>
    <p class="plan-desc">Lorem ipsum dolor sit ametLorem ipsum dolor sit amet, consectetue</p>
    <ul class="plan-features">
      <li><svg width="8" height="6" viewBox="0 0 8 6"><path d="M1 3l2 2 4-4" fill="none" stroke="#fff" stroke-width="1.2"/></svg>5 Times trial</li>
      <li><svg width="8" height="6" viewBox="0 0 8 6"><path d="M1 3l2 2 4-4" fill="none" stroke="#fff" stroke-width="1.2"/></svg>Use all equipments</li>
      <li><svg width="8" height="6" viewBox="0 0 8 6"><path d="M1 3l2 2 4-4" fill="none" stroke="#fff" stroke-width="1.2"/></svg>Advice from trainer</li>
      <li><svg width="8" height="6" viewBox="0 0 8 6"><path d="M1 3l2 2 4-4" fill="none" stroke="#fff" stroke-width="1.2"/></svg>Lorem ipsum dolor</li>
    </ul>
    <div class="plan-btn">REGISTER NOW</div>
  </article>

  <article class="plan" style="left:610px">
    <div class="plan-name">PRO</div>
    <div class="plan-price"><strong>$99</strong><span>/ Month</span></div>
    <p class="plan-desc">Lorem ipsum dolor sit ametLorem ipsum dolor sit amet, consectetue</p>
    <ul class="plan-features">
      <li><svg width="8" height="6" viewBox="0 0 8 6"><path d="M1 3l2 2 4-4" fill="none" stroke="#8dc63f" stroke-width="1.2"/></svg>5 Times trial</li>
      <li><svg width="8" height="6" viewBox="0 0 8 6"><path d="M1 3l2 2 4-4" fill="none" stroke="#8dc63f" stroke-width="1.2"/></svg>Use all equipments</li>
      <li><svg width="8" height="6" viewBox="0 0 8 6"><path d="M1 3l2 2 4-4" fill="none" stroke="#8dc63f" stroke-width="1.2"/></svg>Advice from trainer</li>
      <li><svg width="8" height="6" viewBox="0 0 8 6"><path d="M1 3l2 2 4-4" fill="none" stroke="#8dc63f" stroke-width="1.2"/></svg>Lorem ipsum dolor</li>
      <li><svg width="8" height="6" viewBox="0 0 8 6"><path d="M1 3l2 2 4-4" fill="none" stroke="#8dc63f" stroke-width="1.2"/></svg>Consec</li>
    </ul>
    <div class="plan-btn">REGISTER NOW</div>
  </article>

  <article class="plan" style="left:797px">
    <div class="plan-name">BUSINESS</div>
    <div class="plan-price"><strong>$129</strong><span>/ Month</span></div>
    <p class="plan-desc">Lorem ipsum dolor sit ametLorem ipsum dolor sit amet, consectetue</p>
    <ul class="plan-features">
      <li><svg width="8" height="6" viewBox="0 0 8 6"><path d="M1 3l2 2 4-4" fill="none" stroke="#8dc63f" stroke-width="1.2"/></svg>5 Times trial</li>
      <li><svg width="8" height="6" viewBox="0 0 8 6"><path d="M1 3l2 2 4-4" fill="none" stroke="#8dc63f" stroke-width="1.2"/></svg>Use all equipments</li>
      <li><svg width="8" height="6" viewBox="0 0 8 6"><path d="M1 3l2 2 4-4" fill="none" stroke="#8dc63f" stroke-width="1.2"/></svg>Advice from trainer</li>
      <li><svg width="8" height="6" viewBox="0 0 8 6"><path d="M1 3l2 2 4-4" fill="none" stroke="#8dc63f" stroke-width="1.2"/></svg>Lorem ipsum dolor</li>
      <li><svg width="8" height="6" viewBox="0 0 8 6"><path d="M1 3l2 2 4-4" fill="none" stroke="#8dc63f" stroke-width="1.2"/></svg>Consec</li>
    </ul>
    <div class="plan-btn">REGISTER NOW</div>
  </article>
</section>

<section class="trainers">
  <h2 class="section-title" style="top:67px">OUR TRAINERS</h2>
  <p class="section-sub" style="top:124px">LOREM IPSUM DOLOR SIT AMET</p>

  <article class="trainer trainer-1" style="left:100px">
    <div class="trainer-photo" role="img" aria-label="Portrait of trainer Corwin Brindle with an orange colour overlay"></div>
    <div class="trainer-label" style="top:99px">
      <div class="trainer-role">TRAINER 01</div>
      <div class="trainer-name">CORWIN BRINDLE</div>
      <p class="trainer-bio">Lorem ipsum dolor sit amet, consectetuer adipiscing elit, sed diam nonummy nibh euismod tincidunt ut laoreet dolore</p>
      <div class="trainer-more">MORE INFO</div>
    </div>
  </article>

  <article class="trainer trainer-2" style="left:438px">
    <div class="trainer-photo" role="img" aria-label="Black and white portrait of trainer Tamsin Alcott"></div>
    <div class="trainer-label" style="top:303px">
      <div class="trainer-role">TRAINER 02</div>
      <div class="trainer-name" style="margin-top:6px">TAMSIN ALCOTT</div>
    </div>
  </article>

  <article class="trainer trainer-3" style="left:775px">
    <div class="trainer-photo" role="img" aria-label="Portrait of trainer Odessa Varga in a dark sports top on a light backdrop"></div>
    <div class="trainer-label" style="top:303px">
      <div class="trainer-role">TRAINER 03</div>
      <div class="trainer-name" style="margin-top:6px">ODESSA VARGA</div>
    </div>
  </article>

  <div class="dots"><i class="on"></i><i></i><i></i></div>
</section>

<section class="cta" role="img" aria-label="Athlete stretching with arms raised in a dark gym">
  <div class="cta-lines">
    <div>LOREM</div>
    <div>IPSUM</div>
    <div class="accent">DOLOR</div>
    <div class="accent">SIT AMET</div>
  </div>
  <div class="cta-btn">BOOK SESSION</div>
</section>

<footer class="site-footer">
  <div class="contact-col" style="left:267px">
    <div class="contact-label">MOBILE</div>
    <div class="contact-value">(555) 014-2296</div>
  </div>
  <div class="contact-col" style="left:520px">
    <div class="contact-label">EMAIL</div>
    <div class="contact-value email">corwin@brindlemotioncoaching.example</div>
  </div>
  <div class="contact-col" style="left:772px">
    <div class="contact-label">SOCIAL</div>
    <div class="footer-social">
      <span class="soc-dot"></span><span class="soc-dot"></span><span class="soc-dot"></span>
      <svg width="17" height="12" viewBox="0 0 17 12"><rect x=".5" y=".5" width="16" height="11" rx="1" fill="#cfd0d3"/><path d="M1 1l7.5 6L16 1" fill="none" stroke="#1c1d21" stroke-width="1.3"/></svg>
    </div>
  </div>
  <div class="footer-brand">
    <span class="brand-dot"></span>
    <span class="brand-name">BRINDLE MOTION</span>
  </div>
  <nav class="footer-nav">
    <a href="#">HOME</a><a href="#">ABOUT</a><a href="#">WORKOUTS</a><a href="#">MEMBERSHIP</a><a href="#">SHOP</a><a href="#">CONTACT</a>
  </nav>
</footer>

</body>
</html>
```